Keystone Institute Binder Cover and Spine Design

Design of 1 Binder Cover and Spine -
Dimensions for Colored Print:
Front Cover: 11 1/16 H x 11 1/8 W
Spine: 11 1/16 H x 2 3/8 W
Our Keystone Institute link for more information about the course and the topics covered, as well the background of NGLDA (Northfield Guild of Levy Dispute Advisors). Please take the time to view our website, including the Keystone Institute page to get a background of what the course covers. The website will give you a great feel for what we like in design elements, simple and professional.
https://www.ngldaguild.org/levy-dispute-institute/
Must be included: Blue Logos (all 3)
Words to be included- Keystone Institute (Large- title of course)
-TQB Tax Problem Resolution (Small/Medium Font)
This course attendance includes accountants, Certified Public Accountants, Enrolled Agents, Attorneys and tax professionals. The Keystone Institute instructs them on high level topics of Tax Resolution- which in short is to learn how to legally advocate for your clients and help those with Tax Problems against the TQB.
Attached is our Ground Drill Binder Cover- this is the prerequisite course for the Keystone Institute. We like this design but are looking for something that would be sharper, cleaner and more advanced appeal. This is a professional course and would like the binder cover and spine to reflect that.
Attached are a variety of logos as well. The CPE Logo must be used for our accreditation for the TQB. We do not want any dates on the Binder so we can use over again.
The design we choose, we will need the print PDF as well as the Raw Design File incase we need to edit for size or print.

```html
<!DOCTYPE html>
<html lang="en">
<head>
<meta charset="utf-8">
<title>Keystone Institute Binder Cover and Spine</title>
<link rel="stylesheet" href="https://fonts.googleapis.com/css2?family=Montserrat:wght@400;500;600;800&display=swap">
<style>
  :root {
    --navy: #285a96;
    --navy-deep: #1f4c86;
    --bright-blue: #1c74c4;
    --steel-blue: #6a8cc2;
    --logo-ink: #2b2f6e;
    --paper: #ffffff;
    --backdrop: #ececee;
    --photo-light: #dfe5ec;
    --photo-mid: #9aa8b8;
    --photo-dark: #3b4656;
  }
  * { margin: 0; padding: 0; box-sizing: border-box; }
  html, body {
    width: 1200px;
    height: 842px;
    overflow: hidden;
    background: var(--backdrop);
    font-family: "Montserrat", sans-serif;
  }
  .print-layout {
    position: absolute;
    top: 74px;
    left: 167px;
    display: flex;
    gap: 18px;
  }
  .spine { width: 149px; height: 693px; display: block; }
  .front-cover { width: 698px; height: 693px; display: block; }
  .title-text { font-family: "Montserrat", sans-serif; font-weight: 800; letter-spacing: 0.5px; }
  .subtitle-text { font-family: "Montserrat", sans-serif; font-weight: 400; }
  .org-name { font-family: "Montserrat", sans-serif; font-weight: 600; fill: var(--logo-ink); }
</style>
</head>
<body>
<main class="print-layout">

  <!-- Spine -->
  <svg class="spine" viewBox="0 0 165 770" xmlns="http://www.w3.org/2000/svg">
    <rect width="165" height="770" fill="var(--paper)"/>
    <polygon class="spine-corner-band" points="0,0 165,0 165,140" fill="var(--navy)"/>
    <g class="spine-title" transform="translate(92,205) rotate(90)">
      <text class="title-text" x="0" y="0" font-size="40" fill="var(--navy)">KEYSTONE</text>
      <text class="title-text" x="0" y="42" font-size="40" fill="var(--navy)">INSTITUTE</text>
    </g>
    <text class="org-name" x="82.5" y="588" font-size="22" text-anchor="middle">NGLDA</text>
    <rect class="spine-base-block" x="0" y="620" width="165" height="115" fill="var(--navy)"/>
  </svg>

  <!-- Front cover -->
  <svg class="front-cover" viewBox="0 0 776 770" xmlns="http://www.w3.org/2000/svg">
    <defs>
      <linearGradient id="photoTone" x1="0" y1="0" x2="1" y2="1">
        <stop offset="0" stop-color="var(--photo-light)"/>
        <stop offset="0.55" stop-color="var(--photo-mid)"/>
        <stop offset="1" stop-color="var(--photo-dark)"/>
      </linearGradient>
    </defs>

    <rect width="776" height="770" fill="var(--paper)"/>

    <!-- Photo area -->
    <polygon class="cover-photo" role="img"
      aria-label="Photo of tax professionals reviewing charts on a tablet and laptop at a desk"
      points="0,160 400,0 776,0 776,560 490,770 0,770" fill="url(#photoTone)"/>

    <!-- Crossing blue bands -->
    <polygon class="band-left" points="0,160 75,185 0,300" fill="var(--bright-blue)" opacity="0.9"/>
    <polygon class="band-cross-a" points="400,0 460,0 60,440 0,440 0,380" fill="var(--navy)" opacity="0.45"/>
    <polygon class="band-cross-b" points="0,170 60,170 430,450 360,450" fill="var(--navy)" opacity="0.35"/>
    <polygon class="band-top-right" points="520,0 776,0 776,40 560,0" fill="var(--navy)" opacity="0.5"/>

    <!-- Title field -->
    <polygon class="title-field" points="0,440 420,440 640,640 0,640" fill="var(--navy)" opacity="0.72"/>
    <text class="title-text" x="30" y="545" font-size="64" fill="var(--paper)">KEYSTONE</text>
    <text class="title-text" x="30" y="622" font-size="64" fill="var(--paper)">INSTITUTE</text>

    <!-- Subtitle band -->
    <polygon class="subtitle-band" points="0,640 776,640 776,660 720,700 0,700" fill="var(--navy-deep)"/>
    <text class="subtitle-text" x="48" y="680" font-size="27" fill="var(--paper)">TQB Tax Problem Resolution</text>

    <!-- Lower bands -->
    <polygon class="lower-band" points="0,700 570,700 500,770 0,770" fill="var(--steel-blue)"/>
    <polygon class="lower-white" points="570,700 720,700 776,660 776,770 500,770" fill="var(--paper)"/>
    <polygon class="accent-band" points="490,770 776,555 776,610 560,770" fill="var(--bright-blue)"/>

    <!-- Top-left white field with organisation name -->
    <polygon class="logo-field" points="0,0 400,0 0,160" fill="var(--paper)"/>
    <text class="org-name" x="98" y="50" font-size="26" text-anchor="middle">NGLDA</text>
    <text class="org-name" x="98" y="74" font-size="11" text-anchor="middle">Northfield Guild of</text>
    <text class="org-name" x="98" y="88" font-size="11" text-anchor="middle">Levy Dispute Advisors</text>

    <!-- Accreditation badge placeholder -->
    <rect class="accreditation-badge" x="692" y="705" width="50" height="50" fill="var(--logo-ink)"/>
  </svg>

</main>
</body>
</html>
```